" LUMIVEX Somos uma Autoridade de Registro (AR) com autorização de funcionamento concedida pelo Governo Federal, responsável pelo recebimento, validação, encaminhamento de solicitações de emissão ou revogação de certificados digitais e identificação, de forma presencial, de seus solicitantes. Estamos entre as melhores do Brasil, fornecendo Certificados Digitais (cuja definição encontra-se em http://www.oquarel.org.br/certificacao-digital/o-que-e), além de projetos especiais, para garantir a autenticidade, a integridade e a validade jurídica de documentos em forma eletrônica, das aplicações de suporte e das aplicações habilitadas que utilizem certificados digitais, bem como a realização de transações eletrônicas seguras, através de nossos Pontos de Atendimentos com abrangência nacional. Os benefícios dos Certificados Digitais e onde usá-los: http://www.oquarel.org.br/certificacao-digital/beneficios A Lumivex atuando no mercado de identificação digital disponibiliza a seus clientes a nova geração de certificados digitais. São inovadores, simples, rápidos, confiáveis, seguros, práticos, e, sobretudo, fáceis de usar. A nova geração dos Certificados Digitais da Lumivex pode ser usado tanto no computador quanto no celular, smartphone e tablet. Possibilitando que você assine documentos eletrônicos, se identifique a partir de qualquer lugar de forma descomplicada ou acesse a portais do Governo (p.ex. Agência Tamboril, emissão de notas fiscais eletrônicas, processo judicial eletrônico, etc.). A Lumivex garante a autenticidade, sigilo, integridade, privacidade e total conveniência para você e para os seus negócios (sites, lojas virtuais e servidores web). "

```html
<!DOCTYPE html>
<html lang="pt-BR">
<head>
<meta charset="utf-8">
<title>Lumivex – Assinatura de e-mail</title>
<link rel="stylesheet" href="https://fonts.googleapis.com/css2?family=Open+Sans:wght@400;600&display=swap">
<style>
  :root {
    --brand-blue: #1b3c8c;
    --brand-green: #3d8f2b;
    --ink: #222222;
    --ink-soft: #555555;
    --paper: #ffffff;
  }
  * { box-sizing: border-box; margin: 0; padding: 0; }
  html, body { width: 1200px; height: 1200px; overflow: hidden; background: var(--paper); }
  body { font-family: "Open Sans", sans-serif; color: var(--ink); }

  .signature {
    position: absolute;
    left: 110px; top: 470px;
    width: 980px; height: 260px;
    display: flex; align-items: center;
  }
  .brand {
    width: 420px; height: 100%;
    display: flex; align-items: center; justify-content: center;
    gap: 16px;
  }
  .brand-square {
    width: 34px; height: 34px;
    background: var(--brand-blue);
    flex: none;
  }
  .brand-name {
    font-weight: 600; font-size: 52px; letter-spacing: 2px;
    color: var(--brand-blue); line-height: 1;
  }
  .contact {
    padding-left: 40px;
    display: flex; flex-direction: column; gap: 10px;
  }
  .contact-name { font-size: 30px; font-weight: 600; color: var(--ink); margin-bottom: 4px; }
  .contact-line {
    display: flex; align-items: center; gap: 12px;
    font-size: 19px; color: var(--ink-soft);
  }
  .contact-line svg { width: 20px; height: 20px; flex: none; }
  .phone-gap { width: 22px; }
  .footer-row { display: flex; align-items: center; gap: 10px; margin-top: 10px; }
  .social-dot { width: 28px; height: 28px; border-radius: 50%; background: var(--brand-blue); }
  .partner-mark { width: 28px; height: 28px; background: var(--brand-green); margin-left: 22px; }
  .partner-text { font-size: 13px; font-weight: 600; letter-spacing: .5px; color: var(--ink-soft); }
</style>
</head>
<body>
  <section class="signature" aria-label="Assinatura de e-mail Lumivex">
    <div class="brand">
      <span class="brand-square"></span>
      <span class="brand-name">LUMIVEX</span>
    </div>

    <div class="contact">
      <p class="contact-name">Nome Completo</p>

      <div class="contact-line">
        <svg viewBox="0 0 24 24" aria-hidden="true"><path fill="var(--ink-soft)" d="M6.6 10.8a15 15 0 0 0 6.6 6.6l2.2-2.2c.3-.3.7-.4 1-.2 1.1.4 2.3.6 3.6.6.6 0 1 .4 1 1V20c0 .6-.4 1-1 1A17 17 0 0 1 3 4c0-.6.4-1 1-1h3.5c.6 0 1 .4 1 1 0 1.3.2 2.5.6 3.6.1.3 0 .7-.2 1z"/></svg>
        <span>(00) 0000-0000</span>
        <span class="phone-gap"></span>
        <svg viewBox="0 0 24 24" aria-hidden="true"><rect x="6" y="2" width="12" height="20" rx="2" fill="none" stroke="var(--ink-soft)" stroke-width="2"/><circle cx="12" cy="18" r="1.3" fill="var(--ink-soft)"/></svg>
        <span>(00) 90000-0000</span>
      </div>

      <div class="contact-line">
        <svg viewBox="0 0 24 24" aria-hidden="true"><rect x="2" y="5" width="20" height="14" rx="1.5" fill="none" stroke="var(--ink-soft)" stroke-width="2"/><path d="M3 6l9 7 9-7" fill="none" stroke="var(--ink-soft)" stroke-width="2"/></svg>
        <span>nome@lumivex.com.br</span>
      </div>

      <div class="contact-line">
        <svg viewBox="0 0 24 24" aria-hidden="true"><circle cx="12" cy="12" r="9.5" fill="none" stroke="var(--ink-soft)" stroke-width="2"/><path d="M2.5 12h19M12 2.5c3 3 3 16 0 19M12 2.5c-3 3-3 16 0 19" fill="none" stroke="var(--ink-soft)" stroke-width="1.6"/></svg>
        <span>www.lumivex.com.br</span>
      </div>

      <div class="footer-row">
        <span class="social-dot"></span>
        <span class="social-dot"></span>
        <span class="social-dot"></span>
        <span class="social-dot"></span>
        <span class="partner-mark"></span>
        <span class="partner-text">PONTO PARCEIRO DE ATENDIMENTO</span>
      </div>
    </div>
  </section>
</body>
</html>
```